brevity cafe flyer design project

A funky trendy cafe in Melbourne’s CBD that caters too a large range of corporate clients. Located on the door step of a major train station, its a quick turn around cafe for the short time frame customer but also a cafe to sit, relax and enjoy the hustle and bustle from the inside out. We provide All day breakfast, gourmet sandwiches, gourmet rotti wraps, a la carte menu and also heat and serve meals.

BREAKFAST TO GO! ALL BREAKFAST TO GO ITEMS COME WITH A MEDIUM TAKE AWAY COFFEE!
• RAISIN TOAST & COFFEE – $6
• BACON & EGG MUFFIN & COFFEE $7.5
• SPINACH, MUSHROOM OMELETTE MUFFIN & COFFEE $7.5
• OMELETTE WITH CHEESE MUFFIN & COFFEE $7.5
• HAM & CHEESE CROISSANT & COFFEE $7.5
• SWEET OR SAVOURY MUFFIN & COFFEE $6.5
• HAM & CHEESE SANDWICH & COFFEE $8.0
• HAM, CHEESE & TOMATO SANDWICH & COFFEE $8.5

*NOT IN CONJUNCTION WITH BREVITY CLUB CARD OFFER

WE ALSO HAVE PRE-MADE LUNCH OPTIONS – ASSORTED ROTTI WRAPS (Bbq chicken, honey mustard chicken, pesto chicken & vegetarian) ASSORTED GOURMET SANDWICHES (Mediterranean, Moroccan chicken, Salami, Chicken Schnitzel, Salmon, Brevity & Roast Beef) Soup of the day Pasta of the day Salad of the day

Ph- 03 9718 4630 Fax- 03 9718 4637 Web – www.brevitycafe.com.au 182 DORNAL STREET MELBOURNE 3000

Industry/Entity Type

Cafe

Font styles to use
Serif

Requirements
Must have
• Our 2 branded colours -

PMS 392c
PMS BLACK

```html
<!DOCTYPE html>
<html lang="en">
<head>
<meta charset="utf-8">
<title>Brevity Cafe – Breakfast To Go</title>
<link rel="stylesheet" href="https://fonts.googleapis.com/css2?family=Libre+Baskerville:wght@400;700&family=Oswald:wght@400&family=Josefin+Sans:wght@400;600&family=Delius&display=swap">
<style>
  :root {
    --brand-green: #a4c639;
    --brand-green-dark: #6d8a22;
    --brand-black: #111111;
    --paper-light: #eadfc4;
    --paper-dark: #d3c29c;
    --ink-dark: #1e1a14;
    --ink-brown: #4a1f12;
    --olive: #6e7d3a;
    --contact-brown: #5a3324;
    --contact-text: #f4ece0;
    --strip-grey: #3b3d40;
    --stage: #2a2a2a;
  }
  * { margin: 0; padding: 0; box-sizing: border-box; }
  html, body { width: 1200px; height: 2261px; overflow: hidden; background: var(--stage); }
  .flyer {
    position: absolute; left: 98px; top: 85px; width: 1014px; height: 2085px;
    background: radial-gradient(ellipse at 50% 45%, var(--paper-light) 0%, var(--paper-dark) 100%);
    overflow: hidden;
  }
  .beans-photo {
    position: absolute; left: 0; top: 0; width: 1014px; height: 500px;
    background: linear-gradient(165deg, #3a1f12 0%, #24120a 45%, #5e3f26 78%, var(--paper-dark) 100%);
  }
  .brand-banner { position: absolute; left: 637px; top: 0; width: 311px; height: 450px; }
  .brand-dot {
    position: absolute; left: 771px; top: 185px; width: 44px; height: 44px;
    border-radius: 50%; background: var(--brand-green);
  }
  .brand-name {
    position: absolute; left: 637px; top: 285px; width: 311px; text-align: center; white-space: nowrap;
    font-family: "Josefin Sans", sans-serif; font-weight: 400; font-size: 36px;
    letter-spacing: 1px; color: var(--brand-green);
  }
  .title-ribbon { position: absolute; left: 50px; top: 546px; width: 914px; height: 120px; }
  .title-text {
    position: absolute; left: 0; top: 556px; width: 1014px; text-align: center;
    font-family: "Oswald", sans-serif; font-weight: 400; font-size: 76px; line-height: 92px;
    letter-spacing: 2px; color: var(--brand-black);
  }
  .intro {
    position: absolute; left: 0; top: 685px; width: 1014px; text-align: center;
    font-family: "Libre Baskerville", serif; font-size: 36px; line-height: 54px; color: var(--ink-dark);
  }
  .menu { position: absolute; left: 57px; top: 862px; width: 900px; list-style: none; }
  .menu-item {
    display: flex; align-items: baseline; height: 44px;
    font-family: "Delius", cursive; font-size: 27px; color: var(--ink-dark);
  }
  .menu-item .leader { flex: 1; border-bottom: 2px dotted #8a7a58; margin: 0 4px; transform: translateY(-6px); }
  .offer-note {
    position: absolute; left: 0; top: 1240px; width: 1014px; text-align: center;
    font-family: "Libre Baskerville", serif; font-weight: 700; font-size: 27px; line-height: 38px; color: var(--ink-brown);
  }
  .lunch-heading {
    position: absolute; left: 66px; top: 1352px;
    font-family: "Josefin Sans", sans-serif; font-weight: 400; font-size: 34px; color: var(--olive);
  }
  .lunch-list { position: absolute; left: 66px; top: 1422px; width: 900px; list-style: none; }
  .lunch-item { font-family: "Josefin Sans", sans-serif; font-size: 26px; line-height: 35px; color: var(--ink-dark); text-transform: uppercase; }
  .lunch-detail { font-family: "Josefin Sans", sans-serif; font-size: 17px; line-height: 21px; color: var(--olive); margin-bottom: 4px; }
  .contact-band { position: absolute; left: 0; top: 1818px; width: 1014px; height: 125px; background: var(--contact-brown); }
  .bottom-strip { position: absolute; left: 0; top: 1943px; width: 1014px; height: 142px; background: var(--strip-grey); }
  .wrap-photo {
    position: absolute; left: 400px; top: 1600px; width: 614px; height: 485px;
    border-radius: 55% 35% 0 0 / 45% 30% 0 0;
    background: linear-gradient(160deg, #e6d4ac 0%, #d2b583 30%, #8f9450 62%, #6e4a2e 100%);
  }
  .contact {
    position: absolute; left: 66px; top: 1828px; list-style: none;
    font-family: "Libre Baskerville", serif; font-size: 19px; line-height: 27px; color: var(--contact-text);
  }
  .contact li { display: flex; align-items: flex-start; gap: 10px; }
  .contact svg { flex: none; margin-top: 5px; }
</style>
</head>
<body>
<main class="flyer">
  <div class="beans-photo" role="img" aria-label="Photo of roasted coffee beans spilling from a woven basket"></div>

  <svg class="brand-banner" viewBox="0 0 311 450" aria-hidden="true">
    <polygon points="0,0 311,0 311,330 155,450 0,330" fill="var(--brand-green)"/>
    <polygon points="8,0 303,0 303,325 155,440 8,325" fill="var(--brand-black)"/>
  </svg>
  <div class="brand-dot"></div>
  <div class="brand-name">BREVITY CAFE</div>

  <svg class="title-ribbon" viewBox="0 0 914 120" aria-hidden="true">
    <polygon points="0,30 80,30 80,120 0,120 30,75" fill="var(--brand-green-dark)"/>
    <polygon points="914,30 834,30 834,120 914,120 884,75" fill="var(--brand-green-dark)"/>
    <rect x="50" y="8" width="814" height="96" fill="var(--brand-green)" stroke="var(--brand-green-dark)" stroke-width="3"/>
  </svg>
  <h1 class="title-text">BREAKFAST TO GO!</h1>

  <p class="intro">All Breakfast To Go Items Come With A<br>Medium Take Away Coffeee!</p>

  <ul class="menu">
    <li class="menu-item"><span>Raisin Toast &amp; Coffee</span><span class="leader"></span><span>$6.0</span></li>
    <li class="menu-item"><span>Bacon &amp; Egg Muffin &amp; Coffee</span><span class="leader"></span><span>$7.5</span></li>
    <li class="menu-item"><span>Spinach, Mushroom Omelette Muffin &amp; Coffee</span><span class="leader"></span><span>$7.5</span></li>
    <li class="menu-item"><span>Omelette With Cheese Muffin &amp; Coffee</span><span class="leader"></span><span>$7.5</span></li>
    <li class="menu-item"><span>Ham &amp; Cheese Croissant &amp; Coffee</span><span class="leader"></span><span>$7.5</span></li>
    <li class="menu-item"><span>Sweet Or Savoury Muffin &amp; Coffee</span><span class="leader"></span><span>$6.5</span></li>
    <li class="menu-item"><span>Ham &amp; Cheese Sandwich &amp; Coffee</span><span class="leader"></span><span>$8.0</span></li>
    <li class="menu-item"><span>Ham, Cheese &amp; Tomato Sandwich &amp; Coffee</span><span class="leader"></span><span>$8.5</span></li>
  </ul>

  <p class="offer-note">*NOT IN CONJUNCTION WITH<br>BREVITY CLUB CARD OFFER</p>

  <h2 class="lunch-heading">WE ALSO HAVE PRE-MADE LUNCH OPTIONS –</h2>
  <ul class="lunch-list">
    <li class="lunch-item">Assorted Rotti Wraps</li>
    <li class="lunch-detail">(Bbq chicken, honey mustard chicken, pesto chicken &amp; vegetarian)</li>
    <li class="lunch-item">Assorted Gourmet Sandwiches</li>
    <li class="lunch-detail">(Mediterranean, Moroccan chicken, Salami, Chicken Schnitzel, Salmon, Brevity &amp; Roast<br>Beef).</li>
    <li class="lunch-item">Soup of the day</li>
    <li class="lunch-item">Pasta of the day</li>
    <li class="lunch-item">Salad of the day</li>
  </ul>

  <div class="contact-band"></div>
  <div class="bottom-strip"></div>
  <div class="wrap-photo" role="img" aria-label="Photo of a grilled chicken wrap with lettuce, tomato and red onion on a wooden board"></div>

  <ul class="contact">
    <li>
      <svg width="14" height="18" viewBox="0 0 16 20"><path d="M8 0a7 7 0 0 0-7 7c0 5 7 13 7 13s7-8 7-13a7 7 0 0 0-7-7zm0 10a3 3 0 1 1 0-6 3 3 0 0 1 0 6z" fill="var(--contact-text)"/></svg>
      <span>182 Dornal street,<br>Melbourne 3000</span>
    </li>
    <li>
      <svg width="14" height="16" viewBox="0 0 16 18"><path d="M3 1l3 0 1 4-2 1.5c1 2.5 2.5 4 5 5L11.5 10l4 1v3c0 1-1 2-2 2C6.5 16 1 10.5 1 3c0-1 1-2 2-2z" fill="var(--contact-text)"/></svg>
      <span>03 9718 4630</span>
    </li>
    <li>
      <svg width="14" height="16" viewBox="0 0 16 18"><rect x="1" y="6" width="14" height="9" rx="2" fill="var(--contact-text)"/><rect x="4" y="2" width="8" height="5" fill="var(--contact-text)"/></svg>
      <span>03 9718 4637</span>
    </li>
    <li>
      <svg width="14" height="16" viewBox="0 0 16 16"><circle cx="8" cy="8" r="7" fill="none" stroke="var(--contact-text)" stroke-width="1.6"/><path d="M1 8h14M8 1c3 3 3 11 0 14M8 1c-3 3-3 11 0 14" fill="none" stroke="var(--contact-text)" stroke-width="1.2"/></svg>
      <span>www.brevitycafe.com.au</span>
    </li>
  </ul>
</main>
</body>
</html>
```